五島列島の名産である椿を使った「朱凪しずく水」のラベルデザインを
お願いします。

五島列島のイメージが沸き、椿油を使用しておりますので、高級感がある
デザインを希望します。

具体的な採用イメージが定まっておりませんので、シンプルなデザインから大胆でユニークなものまで、ご自由にデザインして頂ければと思います。
ラベルには、商品名「朱凪しずく水」と「椿油配合」を入れて下さい。

画像添付致しますが、液体の色は椿をイメージして、鮮やかな赤です。

瓶の詳細も添付致します。

何かご不明点ございましたら、お気軽にご連絡下さい。

この商品の魅力である椿色を綺麗に生かして頂いたデザインだった事と
デザインの一部が他の商品にも統一感を出せて展開しやすいと考えました。

本当に良い作品ばかりで、とても悩みました。
教会のステンドグラスや五島列島の島、また観光スポットなど写真を掲載して頂いたりなど、色々調べてデザインを考えて頂いた事に深く感謝致します。
本当にありがとうございました。

```html
<!DOCTYPE html>
<html lang="ja">
<head>
<meta charset="utf-8">
<title>朱凪しずく水 ラベル</title>
<link rel="stylesheet" href="https://fonts.googleapis.com/css2?family=Noto+Serif+JP:wght@400;600;700&family=Tinos:wght@400&display=swap">
<style>
  :root {
    --canvas-bg: #f4f1ec;
    --label-red: #c4122c;
    --label-red-deep: #a50c22;
    --accent-gold: #d8b000;
    --text-light: #ffffff;
    --flower-core: #f7c3cf;
    --flower-mid: #e2456a;
    --flower-edge: #b8143a;
  }
  * { margin: 0; padding: 0; box-sizing: border-box; }
  html, body {
    width: 769px;
    height: 1200px;
    overflow: hidden;
    background: var(--canvas-bg);
  }
  .canvas {
    position: relative;
    width: 769px;
    height: 1200px;
  }
  .label {
    position: absolute;
    left: 154px;
    top: 25px;
    width: 460px;
    height: 1150px;
    background: linear-gradient(180deg, var(--label-red) 0%, var(--label-red-deep) 100%);
    overflow: hidden;
  }
  .label__waves {
    position: absolute;
    inset: 0;
    width: 100%;
    height: 100%;
  }
  .label__english {
    position: absolute;
    top: 210px;
    left: 0;
    width: 100%;
    text-align: center;
    font-family: "Tinos", "Times New Roman", serif;
    font-size: 42px;
    line-height: 50px;
    letter-spacing: 1px;
    color: var(--text-light);
  }
  .label__flower {
    position: absolute;
    left: 120px;
    top: 440px;
    width: 220px;
    height: 220px;
    border-radius: 50%;
    background: radial-gradient(circle at 50% 50%, var(--flower-core) 0%, var(--flower-mid) 38%, var(--flower-edge) 62%, #ffffff 70%, rgba(255,255,255,0.6) 80%, rgba(255,255,255,0) 100%);
  }
  .label__name {
    position: absolute;
    left: 290px;
    top: 680px;
    writing-mode: vertical-rl;
    font-family: "Noto Serif JP", serif;
    font-weight: 700;
    color: var(--text-light);
    letter-spacing: 2px;
  }
  .label__name-lead {
    font-size: 84px;
    line-height: 1.1;
  }
  .label__name-rest {
    font-size: 56px;
    font-weight: 600;
  }
  .label__claim {
    position: absolute;
    right: 30px;
    bottom: 36px;
    font-family: "Noto Serif JP", serif;
    font-size: 30px;
    font-weight: 600;
    color: var(--label-red);
    letter-spacing: 1px;
  }
</style>
</head>
<body>
<div class="canvas">
  <div class="label">
    <svg class="label__waves" viewBox="0 0 460 1150" preserveAspectRatio="none" aria-hidden="true">
      <path fill="var(--accent-gold)" d="M0 0 H460 V70 C400 40 330 30 270 70 C210 110 140 130 80 105 C45 92 20 96 0 110 Z"/>
      <path fill="var(--accent-gold)" d="M0 950 C60 900 130 910 190 960 C250 1010 330 1040 400 1010 C425 1000 445 995 460 1000 V1150 H0 Z"/>
    </svg>
    <div class="label__english">SHUNAGI<br>SHIZUKU<br>WATER</div>
    <div class="label__flower" role="img" aria-label="鮮やかな赤い椿の花の写真"></div>
    <div class="label__name"><span class="label__name-lead">朱</span><span class="label__name-rest">凪しずく水</span></div>
    <div class="label__claim">椿油配合</div>
  </div>
</div>
</body>
</html>
```